Website Design mainly for sliders and icons

Two pages need to be designe, I've finished the templates, all detail requirement please check inattachment:

Mainly design: some pictures/icons and frames

```html
<!DOCTYPE html>
<html lang="en">
<head>
<meta charset="utf-8">
<title>Nimbus Cloud</title>
<link href="https://fonts.googleapis.com/css2?family=Ubuntu:ital,wght@0,300;0,400;0,500;0,700;1,400;1,500&display=swap" rel="stylesheet">
<style>
:root{
  --bg:#f7f6ec;
  --bg-light:#fbfbf6;
  --ink:#333333;
  --muted:#666666;
  --line:#dcdcd4;
  --blue:#2b86d9;
  --blue-dark:#1d6fc2;
  --box:#efede6;
  --map:#a7a7a2;
  --footer:#6b6b6b;
  --footer-ink:#d4d4d4;
}
*{margin:0;padding:0;box-sizing:border-box}
html,body{width:790px;height:1200px;overflow:hidden}
body{font-family:"Ubuntu",sans-serif;color:var(--ink);background:linear-gradient(var(--bg) 0,var(--bg) 320px,var(--bg-light) 420px,#ffffff 700px);position:relative}
.abs{position:absolute}

.topbar{left:0;top:0;width:790px;height:22px;border-bottom:1px solid var(--line)}
.social-top{left:112px;top:0;display:flex;border-left:1px solid var(--line)}
.social-top span{width:23px;height:22px;border-right:1px solid var(--line);display:flex;align-items:center;justify-content:center}
.social-top span i{width:7px;height:7px;background:#b5b5ad;display:block}
.nav{left:420px;top:0;display:flex;font-size:7.5px;letter-spacing:.3px}
.nav a{height:22px;padding:0 10px;display:flex;align-items:center;color:#9a9a92;text-decoration:none;border-left:1px solid var(--line)}
.nav a:last-child{border-right:1px solid var(--line)}
.nav a.active{background:var(--blue);color:#fff;border-color:var(--blue)}

.brand{left:112px;top:40px;display:flex;align-items:center;gap:6px;font-size:20px;font-weight:500;color:var(--blue)}
.brand i{width:14px;height:14px;border-radius:50%;background:var(--blue);display:block}
.contact{left:424px;top:44px;display:flex;gap:16px;font-size:10.5px;font-style:italic;color:#9a9a92}
.contact span{display:flex;align-items:center;gap:6px}

.map{left:124px;top:108px;width:532px;height:168px;border-radius:40px 60px 30px 50px;background:radial-gradient(ellipse at 40% 50%,#b5b5b0,var(--map) 70%,#c4c4be)}
.tagline{left:0;top:286px;width:790px;text-align:center;font-size:16px;font-weight:300;color:#444}
.tagline b{color:var(--blue);font-weight:500}
.hero-shadow{left:0;top:318px;width:790px;height:12px;background:linear-gradient(#e2e2dc,rgba(255,255,255,0))}
.dots{left:379px;top:345px;display:flex;gap:3px}
.dots i{width:8px;height:8px;border-radius:50%;background:#333;display:block}
.dots i:first-child{background:var(--blue)}
.divider{left:132px;top:367px;width:526px;height:1px;background:var(--line)}

.bubble{width:176px;height:68px;background:var(--box);border:1px solid #e2dfd6;border-radius:4px;box-shadow:inset 0 0 0 3px #f6f4ef;display:flex;align-items:center;justify-content:center;text-align:center;font-size:7.5px;line-height:1.4;color:#444;padding:0 14px}
.bubble::after{content:"";position:absolute;bottom:-7px;width:10px;height:10px;background:var(--box);border-right:1px solid #e2dfd6;border-bottom:1px solid #e2dfd6;transform:rotate(45deg)}
.bubble.left::after{right:8px}
.bubble.right::after{left:8px}
.feature-art{left:305px;top:420px;width:170px;height:140px;border-radius:50% 40% 20% 30%;background:radial-gradient(circle at 40% 45%,#e2342c,#c21f1a 45%,rgba(255,255,255,0) 75%)}
.cta{left:310px;top:566px;width:167px;height:22px;background:linear-gradient(#5aa8ec,var(--blue));border:1px solid var(--blue-dark);border-radius:2px;color:#fff;font-size:9.5px;font-weight:500;display:flex;align-items:center;justify-content:center}

.lead-title{left:0;top:606px;width:790px;text-align:center;font-size:16px;font-weight:500;font-style:italic;color:var(--blue)}
.lead-text{left:117px;top:634px;width:556px;text-align:center;font-size:7.3px;line-height:1.35;color:#555}

.service{top:701px;width:177px;height:126px;border:1px solid var(--line);background:#fff;box-shadow:0 1px 2px rgba(0,0,0,.06)}
.service h3{height:41px;border-bottom:1px solid var(--line);display:flex;align-items:center;justify-content:center;gap:6px;font-size:16px;font-weight:500;color:#555}
.service p{padding:11px 10px 0;text-align:center;font-size:7.3px;line-height:1.35;color:#666}

.col-title{top:885px;display:flex;align-items:center;gap:8px;font-size:21px;font-weight:700;color:#333}
.entry{width:260px;display:flex;gap:10px}
.entry .mark{width:88px;flex:none;display:flex;align-items:center;justify-content:center;gap:5px;font-size:13px;font-weight:700;color:var(--blue)}
.entry .mark i{width:10px;height:10px;border-radius:50%;background:var(--blue);display:block;flex:none}
.entry p{font-size:7.3px;line-height:1.35;color:#666}
.entry p b{font-weight:400;color:var(--blue)}

.footer{left:0;top:1176px;width:790px;height:24px;background:var(--footer)}
.footer-info{left:222px;top:1176px;height:24px;display:flex;align-items:center;gap:12px;font-size:7.5px;font-style:italic;color:var(--footer-ink)}
.footer-social{left:570px;top:1176px;display:flex;gap:10px}
.footer-social span{width:24px;height:24px;background:var(--footer);border:1px solid #fff;display:flex;align-items:center;justify-content:center}
.footer-social span i{width:8px;height:8px;background:#fff;display:block}
.footer-gap{left:660px;top:1176px;width:10px;height:24px;background:#fff}
</style>
</head>
<body>

<header>
  <div class="abs topbar"></div>
  <div class="abs social-top" aria-label="Social links"><span><i></i></span><span><i></i></span><span><i></i></span><span><i></i></span></div>
  <nav class="abs nav">
    <a class="active" href="#">HOME</a><a href="#">SOLUTION</a><a href="#">ABOUT US</a><a href="#">CONTACT US</a><a href="#">NEWS</a>
  </nav>
  <div class="abs brand"><i></i>Nimbus Cloud</div>
  <div class="abs contact">
    <span><svg width="8" height="11" viewBox="0 0 8 11"><path d="M2 0 L4 2.5 L3 4 Q3.5 6.5 5 8 L6.5 7 L8 9.5 L6.5 11 Q1 9 0 2 Z" fill="#b0b0a8"/></svg>0800-5550-123-45</span>
    <span><svg width="14" height="10" viewBox="0 0 14 10"><rect width="14" height="10" fill="#b0b0a8"/><path d="M0 0 L7 6 L14 0" fill="none" stroke="#f7f6ec" stroke-width="1.2"/></svg>sales@nimbuscloud.example</span>
  </div>
</header>

<section class="hero">
  <div class="abs map" role="img" aria-label="Grey world map with glowing network nodes linked by thin lines"></div>
  <p class="abs tagline">You can join <b>NimbusCloud</b> Federation and share cloud resource with Others <b>users</b></p>
  <div class="abs hero-shadow"></div>
  <div class="abs dots"><i></i><i></i><i></i></div>
  <div class="abs divider"></div>
</section>

<section class="choice">
  <div class="abs bubble left" style="left:112px;top:407px">We don't want to develop Cloud software by ourselves</div>
  <div class="abs bubble right" style="left:500px;top:407px">We don't want to develop Cloud software by ourselves</div>
  <div class="abs bubble left" style="left:112px;top:507px">We don't want to develop Cloud software by ourselves</div>
  <div class="abs bubble right" style="left:500px;top:507px">We don't want to develop Cloud software by ourselves</div>
  <div class="abs feature-art" role="img" aria-label="Large red question mark with a small white figure sitting on it, thinking"></div>
  <div class="abs cta">PLEASE CHOOSE NIMBUS CLOUD!</div>
</section>

<section class="intro">
  <h2 class="abs lead-title">We can start form scratch and provide a fully cloud enviroment.</h2>
  <p class="abs lead-text">Lorem ipsum dolor sit amet, consectetuer adipiscing elit, sed diam nonummy nibh euismod tincidunt ut laoreet dolore magna aliquam erat volutpat. Ut wisi enim ad minim veniam, quis nostrud exerci tation ullamcorper suscipit lobortis nisl ut aliquip ex ea commodo consequat. Duis autem vel eum iriure dolor in hendrerit in vulputate velit esse molestie consequat, vel illum dolore eu feugiat nulla facilisis at vero eros et accumsan et iusto odio dignissim qui blandit praesent luptatum zzril delenit augue duis dolore te feugait nulla facilisi.</p>
</section>

<section class="services">
  <div class="abs service" style="left:112px">
    <h3><svg width="22" height="26" viewBox="0 0 22 26"><circle cx="11" cy="7" r="6" fill="var(--blue)"/><path d="M0 26 Q0 14 11 14 Q22 14 22 26 Z" fill="var(--blue)"/></svg>Consulting</h3>
    <p>Lorem ipsum dolor sit amet, consecuer adipiscing elit, sed diam nonimy niibh euismod tincidunt ut laoriiieet dolore magna aliquam erat volutpat. Ut wisi enim ad minim veniam, quis nostrud exerci tation facilisi.</p>
  </div>
  <div class="abs service" style="left:305px">
    <h3><svg width="24" height="24" viewBox="0 0 24 24"><path d="M12 3 A9 9 0 1 1 3 12" fill="none" stroke="var(--blue)" stroke-width="4"/><path d="M0 12 L6 12 L3 7 Z" fill="var(--blue)"/></svg>Deploying</h3>
    <p>Lorem ipsum dolor sit amet, consecuer adipiscing elit, sed diam nonimy niibh euismod tincidunt ut laoriiieet dolore magna aliquam erat volutpat. Ut wisi enim ad minim veniam, quis nostrud exerci tation facilisi.</p>
  </div>
  <div class="abs service" style="left:498px">
    <h3><svg width="26" height="26" viewBox="0 0 26 26"><circle cx="13" cy="13" r="10" fill="none" stroke="var(--blue)" stroke-width="5" stroke-dasharray="4 3"/><circle cx="13" cy="13" r="7" fill="none" stroke="var(--blue)" stroke-width="2.5"/><circle cx="13" cy="13" r="3" fill="var(--blue)"/></svg>Integration</h3>
    <p>Lorem ipsum dolor sit amet, consecuer adipiscing elit, sed diam nonimy niibh euismod tincidunt ut laoriiieet dolore magna aliquam erat volutpat. Ut wisi enim ad minim veniam, quis nostrud exerci tation facilisi.</p>
  </div>
</section>

<section class="customers">
  <h2 class="abs col-title" style="left:112px"><svg width="26" height="28" viewBox="0 0 22 26"><circle cx="11" cy="7" r="6" fill="var(--blue)"/><path d="M0 26 Q0 14 11 14 Q22 14 22 26 Z" fill="var(--blue)"/></svg>Our Customers</h2>
  <div class="abs entry" style="left:112px;top:940px"><div class="mark" style="height:40px">Quillcloud</div><p><b>Quill Cloud</b> is dolor sit amet, consecuer adipig elit, sed diam nonimy niibh euivvsmod tincidunt ut laiieet dolore magna aliqvvuam erat volutpat. Ut wisi enim ad minim veniam, quis nostrud exerci tation facilisi.</p></div>
  <div class="abs entry" style="left:112px;top:1019px"><div class="mark" style="height:30px;color:#222"><i style="background:#222"></i>Brinecloud</div><p><b>BrineCloud</b> is dolor sit amet, consecier adipig elit, sed diam nonimy niibh euivvsmod tincidunt ut laiieet dolore magna aliqvvuam erat volutpat. Ut wisi enim ad minim veniam, quis nostrud exerci tation facilisi.</p></div>
  <div class="abs entry" style="left:112px;top:1094px"><div class="mark" style="height:30px;color:#e5892c"><i style="background:#e5892c"></i>Tessiva</div><p><b>Tessiva Network</b> is dolor sit amet, consecuer adipig elit, sed diam nonimy niibh euivvsmod tincidunt ut laiieet dolore magna aliqvvuam erat volutpat. Ut wisi enim ad minim veniam, quis nostrud exerci tation facilisi.</p></div>
</section>

<section class="partners">
  <h2 class="abs col-title" style="left:444px"><svg width="36" height="26" viewBox="0 0 36 26"><path d="M2 8 L12 3 L18 7 L24 3 L34 8 L28 18 L20 23 L8 18 Z" fill="var(--blue)"/></svg>Our Partners</h2>
  <div class="abs entry" style="left:436px;top:940px"><div class="mark" style="height:30px;color:#1b5fa8"><i style="border-radius:0;background:#1b5fa8"></i>varnly</div><p><b>Varnly</b> is dolor sit amet, consecuer adipig elit, sed diam nonimy niibh euivvsmod tincidunt ut laiieet dolore magna aliqvvuam erat volutpat. Ut wisi enim ad minim veniam, quis nostrud exerci tation facilisi.</p></div>
  <div class="abs entry" style="left:436px;top:1019px"><div class="mark" style="height:50px"><i></i>Ostrane</div><p><b>Ostrane Company</b> is dolor sit amet, consecier adipig elit, sed diam nonimy niibh euivvsmod tincidunt ut laiieet dolore magna aliqvvuam erat volutpat. Ut wisi enim ad minim veniam, quis nostrud exerci tation facilisi.</p></div>
</section>

<footer>
  <div class="abs footer"></div>
  <div class="abs footer-info">
    <span>© Copyright 2014, Nimbus Cloud Limited</span>
    <span>0800-5550-123-45</span>
    <span>sales@nimbuscloud.example</span>
  </div>
  <div class="abs footer-social" aria-label="Social links"><span><i></i></span><span><i></i></span><span><i></i></span></div>
  <div class="abs footer-gap"></div>
</footer>

</body>
</html>
```